Stationary Design for Norvath Digital

We are after a full stationary back business cards, letterheads, compliment slip, invoice template, delivery note and anything else we could use within the stationary pack.

We would also like an email footer creating.

Our company details to be included on all stationary:

Registered Name: Norvath Limited
Company Registration Number: 20473915
Website: www.norvathdigital.example
email: info@norvathdigital.example
Phone: 01632 960 417
Address: 48 Tamsin Lane Brellmoor Westvale United Kingdom ZX9 4QT

```html
<!DOCTYPE html>
<html lang="en">
<head>
<meta charset="utf-8">
<title>Norvath Digital – Stationery Pack</title>
<link href="https://fonts.googleapis.com/css2?family=Source+Sans+3:ital,wght@0,400;0,600;0,700;1,700&display=swap" rel="stylesheet">
<style>
:root{
  --navy:#1f3468;
  --slate:#6b7388;
  --ink:#2a2f3c;
  --muted:#6d7280;
  --rule:#c9ccd4;
  --paper:#ffffff;
  --stage-dark:#1f2023;
  --stage-light:#e8e9eb;
  --stage-soft:#e5e6e9;
}
*{box-sizing:border-box;margin:0;padding:0}
html,body{width:1200px;height:2564px;overflow:hidden}
body{font-family:"Source Sans 3",Arial,sans-serif;color:var(--ink);background:var(--stage-light)}

.stage{position:relative;width:1200px;overflow:hidden}
.stage-hero{height:766px;background:var(--stage-dark)}
.stage-range{height:738px;background:var(--stage-light)}
.stage-email{height:274px;background:#fff}
.stage-delivery{height:786px;background:var(--stage-soft)}

.sheet{position:absolute;background:var(--paper);overflow:hidden;display:flex;flex-direction:column;box-shadow:0 3px 10px rgba(0,0,0,.18)}
.band-top{background:var(--slate);flex:none}
.band-bottom{background:var(--navy);flex:none}
.wordmark{font-weight:600;color:var(--navy);letter-spacing:.02em;white-space:nowrap}
.wordmark.on-dark{color:#fff}

.sheet-footer{margin-top:auto;text-align:center;font-size:.72em;line-height:1.45;color:var(--muted);padding:0 2em .9em}
.sheet-footer strong{display:block;color:var(--navy);font-weight:700;font-size:1.15em}
.sheet-footer span{display:block}

/* folder */
.folder{background:var(--slate);display:block}
.folder-disc{position:absolute;border-radius:50%;background:var(--navy)}
.folder .wordmark{position:absolute}
.folder-hero{left:50px;top:60px;width:420px;height:640px}
.folder-hero .folder-disc{width:560px;height:560px;left:-10px;top:30px}
.folder-hero .wordmark{font-size:40px;left:78px;top:284px}
.folder-range{left:790px;top:240px;width:350px;height:480px}
.folder-range .folder-disc{width:700px;height:700px;left:40px;top:-110px}
.folder-range .wordmark{font-size:32px;left:90px;top:216px}

/* letterhead */
.letterhead .band-top{height:1.8em}
.letterhead .band-bottom{height:1.6em}
.letterhead .wordmark{font-size:2.3em;text-align:center;margin-top:1.1em}
.letter-body{padding:3.4em 5em 0;font-size:.95em;line-height:1.5;color:var(--ink)}
.letter-body p{margin-bottom:1.1em}
.letter-costs{width:100%;border-collapse:collapse;margin:0 0 1.2em}
.letter-costs td{border-bottom:1px solid var(--rule);padding:.15em 0;font-size:.9em}
.letter-costs td:last-child{text-align:right}
.letter-sign{margin-top:2em;color:var(--navy);font-weight:600}
.letterhead-hero{left:500px;top:60px;width:320px;height:440px;font-size:5.7px}
.letterhead-range{left:425px;top:240px;width:350px;height:480px;font-size:6.2px}

/* business cards */
.card{width:300px;height:171px}
.card-front .band-top{height:9px}
.card-front .band-bottom{height:12px}
.card-front-body{flex:1;display:flex;align-items:center;padding:0 18px}
.card-front .wordmark{font-size:19px;flex:none;width:128px}
.card-divider{width:1px;height:78px;background:var(--rule);margin:0 14px;flex:none}
.card-contact{font-size:7.5px;line-height:1.5;color:var(--muted)}
.card-contact strong{display:block;color:var(--navy);font-size:10px;font-weight:700}
.card-contact em{display:block;font-style:normal;margin-bottom:4px}
.card-back{background:var(--slate);display:block}
.card-back .folder-disc{width:250px;height:250px;left:-40px;top:-40px}
.card-back .wordmark{position:absolute;left:26px;top:72px;font-size:20px}
.card-hero-front{left:850px;top:60px}
.card-hero-back{left:850px;top:261px}
.card-delivery-front{left:830px;top:70px}
.card-delivery-back{left:830px;top:270px}

/* envelopes */
.envelope .band-top{height:6px}
.envelope .band-bottom{height:8px}
.envelope .wordmark{margin:18px 0 0 24px}
.envelope-return{margin:auto 0 10px 24px;font-size:5.5px;line-height:1.45;color:var(--muted)}
.envelope-hero{left:500px;top:530px;width:650px;height:186px}
.envelope-hero .wordmark{font-size:22px}
.envelope-hero .envelope-return{font-size:6.5px}
.envelope-range{left:790px;top:34px;width:350px;height:180px}
.envelope-range .wordmark{font-size:17px}
.envelope-flapside{left:425px;top:34px;width:350px;height:180px;display:block}
.envelope-flapside svg{display:block}

/* compliment slip */
.comp-slip{left:60px;top:34px;width:350px;height:180px;font-size:6px}
.comp-slip .band-top{height:8px}
.comp-slip .band-bottom{height:9px}
.comp-head{display:flex;justify-content:space-between;align-items:center;padding:14px 20px 0}
.comp-head .wordmark{font-size:17px}
.comp-title{font-style:italic;font-weight:700;color:var(--navy);font-size:10px}
.comp-slip .sheet-footer{padding-bottom:6px}

/* invoice & delivery note */
.invoice{left:60px;top:240px;width:350px;height:480px;font-size:6.2px}
.delivery-note{left:320px;top:40px;width:460px;height:650px;font-size:8.1px}
.doc .band-top{height:1.9em}
.doc .band-bottom{height:1.7em}
.doc .wordmark{font-size:2.2em;text-align:center;margin-top:1em}
.doc-head{display:flex;justify-content:space-between;padding:2.2em 3.2em 0}
.doc-to{font-size:.85em;line-height:1.45;color:var(--muted)}
.doc-to b{display:block;color:var(--navy);font-size:1.2em}
.doc-meta{text-align:center}
.doc-title{color:var(--navy);font-weight:700;font-size:2em;letter-spacing:.04em}
.doc-meta table{border-collapse:collapse;margin-top:.4em}
.doc-meta td{border:1px solid var(--rule);padding:.3em .8em;font-size:.8em;text-align:left;line-height:1.3}
.doc-meta td b{display:block;color:var(--navy)}
.doc-items{margin:2.2em 3.2em 0;width:calc(100% - 6.4em);border-collapse:collapse;font-size:.82em}
.doc-items th{background:var(--navy);color:#fff;font-weight:600;padding:.6em .5em;text-align:center}
.doc-items td{border:1px solid var(--rule);padding:.85em .5em;text-align:center}
.doc-items td.desc{text-align:left}
.doc-lower{display:flex;justify-content:space-between;padding:1.2em 3.2em 0;align-items:flex-start}
.doc-notes{font-size:.72em;line-height:1.5;color:var(--muted)}
.doc-notes b{color:var(--navy)}
.doc-totals{border-collapse:collapse;font-size:.8em}
.doc-totals td{padding:.3em .8em;text-align:right;border-bottom:1px solid var(--rule)}
.doc-totals tr.grand td{background:var(--navy);color:#fff;font-weight:700}
.doc-thanks{text-align:center;color:var(--navy);font-weight:700;font-size:1.05em;margin:auto 0 .9em}
.doc .sheet-footer{margin-top:0}

/* email footer */
.email-label{position:absolute;left:940px;top:22px;font-size:21px;color:#8a8f9a}
.email-mark{position:absolute;left:182px;top:62px;width:330px;height:150px;background:var(--navy);display:flex;align-items:center;justify-content:center}
.email-mark .wordmark{font-size:34px}
.email-rule{position:absolute;left:540px;top:56px;width:2px;height:162px;background:var(--rule)}
.email-details{position:absolute;left:566px;top:92px;font-size:17px;line-height:1.35;color:var(--slate)}
.email-details strong{display:block;color:var(--navy);font-weight:700}
.email-details .email-contact{color:var(--navy)}

.delivery-label{position:absolute;left:86px;top:598px;font-size:24px;color:var(--navy);font-weight:600}
</style>
</head>
<body>

<section class="stage stage-hero">
  <div class="sheet folder folder-hero">
    <div class="folder-disc"></div>
    <div class="wordmark on-dark">Norvath Digital</div>
  </div>

  <div class="sheet letterhead letterhead-hero">
    <div class="band-top"></div>
    <div class="wordmark">Norvath Digital</div>
    <div class="letter-body">
      <p>Dear Client,</p>
      <p>Lorem ipsum dolor sit amet, consectetur adipiscing elit. Nunc vel urna finibus, sollicitudin massa at, molestie ante. Vestibulum at scelerisque elit, tincidunt id nibh.</p>
      <p>Aliquam erat volutpat. Praesent fringilla ante vel purus hendrerit, eu fermentum leo posuere. Donec tempor ligula sit amet fringilla scelerisque.</p>
      <p>Nullam in mi felis. Mauris sit amet lobortis ex, a pellentesque nulla.</p>
      <div class="letter-sign">Kind regards,<br>Norvath Limited</div>
    </div>
    <div class="sheet-footer"><strong>Norvath Limited</strong><span>Address : 48 Tamsin Lane Brellmoor Westvale United Kingdom ZX9 4QT</span><span>Company Registration Number : 20473915 • Tel : 01632 960 417 • Website : www.norvathdigital.example • Email : info@norvathdigital.example</span></div>
    <div class="band-bottom"></div>
  </div>

  <div class="sheet card card-front card-hero-front">
    <div class="band-top"></div>
    <div class="card-front-body">
      <div class="wordmark">Norvath Digital</div>
      <div class="card-divider"></div>
      <div class="card-contact"><strong>Aidan Marlow</strong><em>Director</em>T : 01632 960 417<br>E : info@norvathdigital.example<br>W : www.norvathdigital.example<br>48 Tamsin Lane Brellmoor<br>Westvale ZX9 4QT</div>
    </div>
    <div class="band-bottom"></div>
  </div>
  <div class="sheet card card-back card-hero-back">
    <div class="folder-disc"></div>
    <div class="wordmark on-dark">Norvath Digital</div>
  </div>

  <div class="sheet envelope envelope-hero">
    <div class="band-top"></div>
    <div class="wordmark">Norvath Digital</div>
    <div class="envelope-return">If undelivered, please return to:<br>48 Tamsin Lane Brellmoor Westvale<br>United Kingdom ZX9 4QT</div>
    <div class="band-bottom"></div>
  </div>
</section>

<section class="stage stage-range">
  <div class="sheet comp-slip">
    <div class="band-top"></div>
    <div class="comp-head"><div class="wordmark">Norvath Digital</div><div class="comp-title">With Compliments</div></div>
    <div class="sheet-footer"><strong>Norvath Limited</strong><span>Address : 48 Tamsin Lane Brellmoor Westvale United Kingdom ZX9 4QT</span><span>Company Registration Number : 20473915 • Tel : 01632 960 417 • Website : www.norvathdigital.example • Email : info@norvathdigital.example</span></div>
    <div class="band-bottom"></div>
  </div>

  <div class="sheet envelope-flapside">
    <svg width="350" height="180" viewBox="0 0 350 180" aria-hidden="true">
      <polygon points="0,0 350,0 240,52 110,52" fill="#6b7388"/>
    </svg>
  </div>

  <div class="sheet envelope envelope-range">
    <div class="band-top"></div>
    <div class="wordmark">Norvath Digital</div>
    <div class="envelope-return">If undelivered, please return to:<br>48 Tamsin Lane Brellmoor Westvale<br>United Kingdom ZX9 4QT</div>
    <div class="band-bottom"></div>
  </div>

  <div class="sheet doc invoice">
    <div class="band-top"></div>
    <div class="wordmark">Norvath Digital</div>
    <div class="doc-head">
      <div class="doc-to">To<b>Aidan Marlow</b>Unit 7, 2nd Floor, Harrow Court,<br>Westbury, United Kingdom<br>Tel : +44 1632 960 882</div>
      <div class="doc-meta">
        <div class="doc-title">INVOICE</div>
        <table><tr><td><b>Number</b>INV 508 72</td><td><b>Date</b>20/06/2016</td><td><b>Due Date</b>20/07/2016</td></tr></table>
      </div>
    </div>
    <table class="doc-items">
      <tr><th>S. NO</th><th>Item description</th><th>Unit</th><th>Unit Price</th><th>Total</th></tr>
      <tr><td>1.</td><td class="desc">Set Design/Development &amp; Shoot</td><td>1</td><td>21,000</td><td>21,000.00</td></tr>
      <tr><td>2.</td><td class="desc">Photography</td><td>2</td><td>10000</td><td>20,000.00</td></tr>
      <tr><td>3.</td><td class="desc">Transport</td><td>1</td><td>10,000</td><td>10,000.00</td></tr>
      <tr><td>4.</td><td class="desc">Materials</td><td>5</td><td>1000</td><td>5,000.00</td></tr>
      <tr><td>5.</td><td class="desc">Design</td><td>1</td><td>1000</td><td>1,000.00</td></tr>
    </table>
    <div class="doc-lower">
      <div class="doc-notes"><b>Payment Methods</b><br>Email : info@norvathdigital.example<br>We accept cards and bank transfer<br><br><b>Terms &amp; Conditions</b><br>1. Terms &amp; Condition One here<br>2. Terms &amp; Condition Two here<br>3. Terms &amp; Condition Three here</div>
      <table class="doc-totals">
        <tr><td>SUBTOTAL</td><td>57,000.00</td></tr>
        <tr><td>TAX (6%)</td><td>3,420.00</td></tr>
        <tr class="grand"><td>TOTAL</td><td>60,420.00</td></tr>
      </table>
    </div>
    <div class="doc-thanks">THANK YOU FOR YOUR BUSINESS</div>
    <div class="sheet-footer"><strong>Norvath Limited</strong><span>Address : 48 Tamsin Lane Brellmoor Westvale United Kingdom ZX9 4QT</span><span>Company Registration Number : 20473915 • Tel : 01632 960 417 • Website : www.norvathdigital.example • Email : info@norvathdigital.example</span></div>
    <div class="band-bottom"></div>
  </div>

  <div class="sheet letterhead letterhead-range">
    <div class="band-top"></div>
    <div class="wordmark">Norvath Digital</div>
    <div class="letter-body">
      <p>Lorem ipsum dolor sit amet, consectetur adipiscing elit. Nunc vel urna finibus, sollicitudin massa at, molestie ante. Vestibulum at scelerisque elit, tincidunt id nibh. Maecenas pulvinar rutrum metus, vel aliquet ante euismod sed.</p>
      <p>Aliquam erat volutpat. Praesent fringilla ante vel purus hendrerit, eu fermentum leo posuere. Donec tempor ligula sit amet fringilla scelerisque. Aliquam erat volutpat, et sodales libero.</p>
      <table class="letter-costs">
        <tr><td>Vitae mattis magna tempus</td><td>00,000</td></tr>
        <tr><td>Mattis magna tristique</td><td>00,000</td></tr>
        <tr><td>Magna tempus</td><td>00,000</td></tr>
        <tr><td>Tristique mattis magna</td><td>00,000</td></tr>
        <tr><td>Cras mattis magna tempus</td><td>00,000</td></tr>
        <tr><td>Vitae mattis tristique</td><td>00,000</td></tr>
      </table>
      <p>Nullam in mi felis. Mauris sit amet lobortis ex, a pellentesque nulla. Lorem ipsum dolor sit amet, consectetur adipiscing elit.</p>
    </div>
    <div class="sheet-footer"><strong>Norvath Limited</strong><span>Address : 48 Tamsin Lane Brellmoor Westvale United Kingdom ZX9 4QT</span><span>Company Registration Number : 20473915 • Tel : 01632 960 417 • Website : www.norvathdigital.example • Email : info@norvathdigital.example</span></div>
    <div class="band-bottom"></div>
  </div>

  <div class="sheet folder folder-range">
    <div class="folder-disc"></div>
    <div class="wordmark on-dark">Norvath Digital</div>
  </div>
</section>

<section class="stage stage-email">
  <div class="email-label">Email footer</div>
  <div class="email-mark"><div class="wordmark on-dark">Norvath Digital</div></div>
  <div class="email-rule"></div>
  <div class="email-details">
    <strong>Norvath Limited</strong>
    Address : 48 Tamsin Lane Brellmoor Westvale<br>
    United Kingdom ZX9 4QT<br>
    <span class="email-contact">T : 01632 960 417 | W : www.norvathdigital.example</span>
  </div>
</section>

<section class="stage stage-delivery">
  <div class="sheet doc delivery-note">
    <div class="band-top"></div>
    <div class="wordmark">Norvath Digital</div>
    <div class="doc-head">
      <div class="doc-to">To<b>Aidan Marlow</b>Unit 7, 2nd Floor, Harrow Court,<br>Westbury, United Kingdom<br>Tel : +44 1632 960 882</div>
      <div class="doc-meta">
        <div class="doc-title">Delivery Note</div>
        <table><tr><td><b>Order no.</b>DN 15.04.99</td><td><b>Order Date</b>07/06/2016</td></tr></table>
      </div>
    </div>
    <table class="doc-items">
      <tr><th>S. NO</th><th>Item description</th><th>QTY</th></tr>
      <tr><td>1.</td><td class="desc">Item 1</td><td>2</td></tr>
      <tr><td>2.</td><td class="desc">Item 2</td><td>1</td></tr>
      <tr><td>3.</td><td class="desc">Item 3</td><td>4</td></tr>
      <tr><td>4.</td><td class="desc">Item 4</td><td>1</td></tr>
    </table>
    <div class="doc-lower">
      <div class="doc-notes"><b>Payment Methods</b><br>Email : info@norvathdigital.example<br>We accept cards and bank transfer<br><br><b>Terms &amp; Conditions</b><br>1. Terms &amp; Condition One here, to be edited<br>2. Terms &amp; Condition Two here, to be edited<br>3. Terms &amp; Condition Three here, sample text</div>
    </div>
    <div class="doc-thanks">THANK YOU FOR YOUR BUSINESS</div>
    <div class="sheet-footer"><strong>Norvath Limited</strong><span>Address : 48 Tamsin Lane Brellmoor Westvale United Kingdom ZX9 4QT</span><span>Company Registration Number : 20473915 • Tel : 01632 960 417 • Website : www.norvathdigital.example • Email : info@norvathdigital.example</span></div>
    <div class="band-bottom"></div>
  </div>

  <div class="sheet card card-front card-delivery-front">
    <div class="band-top"></div>
    <div class="card-front-body">
      <div class="wordmark">Norvath Digital</div>
      <div class="card-divider"></div>
      <div class="card-contact"><strong>Aidan Marlow</strong><em>Director</em>T : 01632 960 417<br>E : info@norvathdigital.example<br>W : www.norvathdigital.example<br>48 Tamsin Lane Brellmoor<br>Westvale ZX9 4QT</div>
    </div>
    <div class="band-bottom"></div>
  </div>
  <div class="sheet card card-back card-delivery-back">
    <div class="folder-disc"></div>
    <div class="wordmark on-dark">Norvath Digital</div>
  </div>

  <div class="delivery-label">Delivery note</div>
</section>

</body>
</html>
```